DL Flyer Design

I need a DL flyer, double-sided designed for a Brisbane based outdoor group exercise/training company called Step Up! Step Up! provides group outdoor training, designed for the individual. It provides the support, motivation and one-on-one attention of personal training combined with the support of a group environment. The classes are fun, challenging and aim to develop confidence & fitness. Weight loss is not the focus, although it is a benefit.
Updates

Hi

I've just uploaded a high res version of the logo if you need.

Cheers
Tam

Target Market(s)

English speaking men & women aged 25 - 45, white-collar office jobs. Average-low level of fitness, not hugely 'fitness' oriented but want to improve quality of life, overall fitness, lose a bit of weight.

Computer and consumer literate. Live in suburban Brisbane, Australia.

Industry/Entity Type

Training

Requirements
Must have
• Double sided DL. Use of black, greens and white per attached photos. Use of 1300 572 914 (1300 STEP UP) and website www.stepupactive.example.au

Indicative copy and contents is posted in the comments section.

```html
<!DOCTYPE html>
<html lang="en">
<head>
<meta charset="utf-8">
<title>Step Up! – Class Timetable Flyer</title>
<link rel="stylesheet" href="https://fonts.googleapis.com/css2?family=Arimo:wght@400;700&display=swap">
<style>
  :root {
    --green-deep: #00a33b;
    --green-table: #1ea03a;
    --green-lime: #8cc63f;
    --green-web: #3cb54a;
    --row-pale: #f3f8fb;
    --ink: #111111;
    --paper: #ffffff;
  }
  * { margin: 0; padding: 0; box-sizing: border-box; }
  html, body { width: 1200px; height: 602px; overflow: hidden; background: var(--paper); }
  body { font-family: "Arimo", Arial, sans-serif; color: var(--ink); }

  .flyer { position: relative; width: 1200px; height: 602px; overflow: hidden; background: var(--paper); }

  .colour-block { position: absolute; left: 0; top: 0; }

  .hero-figure {
    position: absolute; left: 836px; top: 0; width: 364px; height: 362px;
    background: linear-gradient(135deg, #ffffff 0%, #eef7e0 45%, #cfe8a6 100%);
  }

  .timetable {
    position: absolute; left: 30px; top: 125px; width: 780px; height: 240px;
    background: var(--green-table); border-radius: 6px;
  }
  .timetable .row { position: absolute; left: 5px; width: 770px; }
  .row--head { top: 0; height: 35px; }
  .row--morning { top: 35px; height: 66px; background: var(--green-lime); }
  .row--midday { top: 101px; height: 66px; background: var(--row-pale); }
  .row--evening { top: 167px; height: 67px; background: var(--green-lime); }

  .cell { position: absolute; font-size: 19px; line-height: 1.1; color: var(--ink); }
  .row--head .cell { top: 9px; font-size: 20px; color: var(--paper); }
  .cell--time { font-weight: 700; }
  .cell--small { font-size: 15.5px; line-height: 1.22; }
  .row--morning .cell, .row--evening .cell { top: 7px; }
  .row--midday .cell { top: 6px; }
  .row--evening .cell--small { top: 5px; }

  .offer { position: absolute; left: 256px; font-size: 17px; color: var(--ink); white-space: nowrap; }
  .offer--note { top: 459px; }
  .offer--contact { top: 493px; }
  .offer--web { top: 530px; left: 261px; font-size: 19.5px; font-weight: 700; color: var(--green-web); }

  .brand {
    position: absolute; left: 50px; top: 484px;
    display: flex; align-items: center; gap: 10px;
  }
  .brand__dot { width: 22px; height: 22px; border-radius: 50%; background: var(--ink); }
  .brand__name { font-size: 38px; font-weight: 700; color: var(--green-lime); letter-spacing: -0.5px; }
</style>
</head>
<body>
<main class="flyer">
  <svg class="colour-block" width="1200" height="602" viewBox="0 0 1200 602" aria-hidden="true">
    <path d="M586 110 Q586 90 606 90 L836 90 L836 362 L1200 362 L1200 602 L586 602 Z" fill="var(--green-deep)"/>
  </svg>

  <div class="hero-figure" role="img" aria-label="Lime green silhouette of a woman leaping with arms outstretched"></div>

  <section class="timetable" aria-label="Weekly class timetable">
    <div class="row row--head">
      <span class="cell" style="left:9px">Time</span>
      <span class="cell" style="left:95px">Monday</span>
      <span class="cell" style="left:200px">Tuesday</span>
      <span class="cell" style="left:317px">Wednesday</span>
      <span class="cell" style="left:460px">Thursday</span>
      <span class="cell" style="left:579px">Friday</span>
      <span class="cell" style="left:673px">Saturday</span>
    </div>
    <div class="row row--morning">
      <span class="cell cell--time" style="left:8px">6.00am</span>
      <span class="cell" style="left:96px">Cardio</span>
      <span class="cell cell--small" style="left:317px">Stress-<br>relief<br>(boxing!)</span>
      <span class="cell" style="left:463px">Cardio</span>
      <span class="cell cell--small" style="left:579px">Stress-<br>relief<br>(boxing!)</span>
      <span class="cell" style="left:672px">Mash-up</span>
    </div>
    <div class="row row--midday">
      <span class="cell cell--small" style="left:673px">One-on-<br>One<br>sessions</span>
    </div>
    <div class="row row--evening">
      <span class="cell cell--time" style="left:8px">6.00pm</span>
      <span class="cell" style="left:96px">Strength</span>
      <span class="cell" style="left:209px">Cardio</span>
      <span class="cell" style="left:317px">Strength</span>
      <span class="cell cell--small" style="left:463px">Stress-<br>relief<br>(boxing!)</span>
    </div>
  </section>

  <div class="brand">
    <span class="brand__dot" aria-hidden="true"></span>
    <span class="brand__name">Step Up!</span>
  </div>

  <p class="offer offer--note">(Guaranteed no hard sell at the end)</p>
  <p class="offer offer--contact">Call now on 1300 STEP UP (1300 572 914) or email hello@stepupactive.example.au.</p>
  <p class="offer offer--web">www.stepupactive.example.au</p>
</main>
</body>
</html>
```